Manufacturing Company WordPress Website Design

Looking for a modern WordPress design for a manufacturer of oil separation and coolant recycling products called BrightFloe. This is a business-to-business marketer in the industrial manufacturing sector. BrightFloe sells to CNC manufacturing companies and their products are known as some of the best tools in the world for skimming and separating floating oils, metallic fines, and other contaminants from industrial process fluids.

The winning design will be based on a responsive WP theme. Include the theme name if your design is selected by the client. Provide Home, Product and Case Study page views with your submission.

THE BRIGHTFLOE BRAND
The BrightFloe brand is all about connection and partnership. They are down-to-earth, relatable, helpful and fun to hang out with. The brand voice is humble, authentic and helpful and they are driven by connection, togetherness and inclusion.

The BrightFloe target audience is plant managers, enterprise engineers and business owners in CNC machining manufacturing companies across a variety of industries (automotive, aerospace, energy, medical and transportation).

BrightFloe is looking for a clean, modern website that better represents their brand with a more polished and professional design. It should be:
- responsive and mobile-friendly
- easily findable for key search criteria
- a source for improved lead generation for prospective sales
- more easily editable

A design that is oriented toward these goals will be selected as the winner.

The winning designer may be chosen to code the website, or to code the initial pages in the concept design.

Current Website:
https://brightfloe-example.com/index.html

Competitors:
https://www.kelvora-example.com/
https://www.tundix-example.com/
https://www.voltarin-example.com/

Sites We Like:
https://northgateweldworks-example.com/
- we like the clean layout of the home page in a grid-like design, simple header and footer, the parallax scrolling, and the mobile responsiveness.

https://www.kelvora-example.com/fluid-filtration/sentinel-coolant-recycling-systems/
- we like the way the content is presented on the Kelvora product page - specifically, we like the use of the tabs below the main product images to present a lot of content without it looking overwhelmingly busy.

https://pinecrestpanes-example.com/healthcare/harborview-care-clinic/
- we like the way Pinecrest Panes presents their cases studies with a combination of useful information highlighted by informative icons and pictures to present key statistics in the case study. We would like the BrightFloe case studies to almost feel like an infographic presentation on the website.

Attached files to help your designs:
- Brand Identity Guidelines
- BrightFloe Logos
- Product Photos
- Brand Photos
- Home page content
- Coolant Recycling product page content
- Case Study page content
- Site Map
- Wire Frames

Target Market(s)

Industry/Entity Type

Industrial

Coding

Coded - Design and coding required

Number of Pages Required

3 page

Font styles to use
Sans Serif
Other font styles liked:
• DINPro is used on all collateral - see brand guidelines

Requirements
Must have
• See the brand guidelines file attached for colors and logo usage

```html
<!DOCTYPE html>
<html lang="en">
<head>
<meta charset="utf-8">
<title>BrightFloe – Coolant Recycling System</title>
<link href="https://fonts.googleapis.com/css2?family=Barlow:wght@400;500;600;700&family=Lato:wght@400;700&display=swap" rel="stylesheet">
<style>
:root{
  --red:#c8161d;
  --ink:#1b1b1b;
  --text:#2a2a2a;
  --navy:#1f3f73;
  --dark:#1c1f24;
  --line:#d6d6d6;
  --white:#ffffff;
}
*{box-sizing:border-box;margin:0;padding:0}
html,body{width:1200px;height:2683px;overflow:hidden;background:var(--white)}
body{position:relative;font-family:"Lato",sans-serif;color:var(--text)}
.abs{position:absolute}
.btn{position:absolute;background:var(--red);color:var(--white);font-family:"Barlow",sans-serif;font-weight:700;font-size:14px;letter-spacing:.5px;display:flex;align-items:center;justify-content:center;text-transform:uppercase}

/* header */
.brand{left:75px;top:12px;display:flex;align-items:center;gap:10px}
.brand-mark{width:72px;height:72px;border-radius:50%;background:var(--navy)}
.brand-name{font-family:"Barlow",sans-serif;font-weight:700;font-size:36px;color:var(--navy);line-height:1}
.brand-tag{font-size:10px;color:var(--navy);margin-top:3px}
.phone{left:640px;top:14px;display:flex;align-items:center;gap:10px;font-family:"Barlow",sans-serif;font-weight:600;font-size:23px;color:var(--ink)}
.mail{left:868px;top:20px}
.estimate{left:918px;top:0;width:282px;height:53px;background:var(--red);color:var(--white);font-family:"Barlow",sans-serif;font-weight:600;font-size:17px;display:flex;align-items:center;padding-left:22px;gap:22px}
.nav{top:84px;right:77px;display:flex;gap:37px;font-family:"Barlow",sans-serif;font-size:17px;color:var(--ink)}

/* hero */
.hero{left:0;top:126px;width:1200px;height:511px;background:linear-gradient(100deg,#6b4a3a 0%,#5c5f66 35%,#7b7f86 70%,#4c5057 100%)}
.hero-title{top:322px;width:1200px;text-align:center;font-family:"Barlow",sans-serif;font-weight:700;font-size:52px;color:var(--white)}

/* product cards */
.card{position:absolute;top:581px;width:328px;background:var(--white);box-shadow:0 2px 10px rgba(0,0,0,.14);text-align:center}
.card h3{font-family:"Barlow",sans-serif;font-weight:600;font-size:22px;color:var(--ink);margin-top:30px;line-height:27px;padding:0 40px}
.card .shot{position:absolute;left:24px;width:280px;border-radius:4px}
.card p{position:absolute;left:22px;width:284px;font-size:14.5px;line-height:22px;color:var(--ink)}
.card .btn{width:141px;height:37px;left:93px}

/* trusted */
.section-title{width:1200px;text-align:center;font-family:"Barlow",sans-serif;font-weight:700;font-size:34px;color:var(--ink)}
.logo-box{position:absolute;top:1341px;width:179px;height:104px;border:1px solid #cfcfcf;display:flex;align-items:center;justify-content:center;font-family:"Lato",sans-serif;font-weight:700;font-size:17px;color:var(--navy);gap:8px}
.arrow{position:absolute;top:1371px;width:42px;height:38px;background:var(--red);display:flex;align-items:center;justify-content:center}

/* roi */
.roi{left:0;top:1518px;width:1200px;height:367px;background:linear-gradient(120deg,#2a2d33,#15181c 60%,#23262b)}
.roi-text{left:270px;top:1660px;width:660px;text-align:center;color:#e4e4e4;font-size:16px;line-height:28px}

/* case study */
.case-client{left:220px;top:2058px;width:184px;height:77px;display:flex;align-items:center;justify-content:center;font-family:"Lato",sans-serif;font-weight:700;font-size:30px;color:var(--ink)}
.case-text{left:479px;top:2050px;width:540px;font-size:19.5px;line-height:28px;color:var(--ink)}

/* newsletter */
.news{left:0;top:2303px;width:1200px;height:212px;background:linear-gradient(120deg,#4a3f26,#22252a 50%,#1c1f24)}
.news-title{left:78px;top:2378px;font-family:"Barlow",sans-serif;font-weight:700;font-size:27px;color:var(--white)}
.news-title span{color:var(--red)}
.news-sub{left:78px;top:2413px;font-family:"Barlow",sans-serif;font-size:17px;letter-spacing:1px;color:var(--white)}
.news-rule{left:565px;top:2376px;width:1px;height:62px;background:var(--red)}
.email{left:591px;top:2384px;width:360px;height:46px;background:var(--white);font-size:15px;color:var(--ink);display:flex;align-items:center;padding-left:30px}
.subscribe{left:951px;top:2384px;width:159px;height:46px;font-size:18px}

/* footer */
.foot-links{left:84px;top:2576px;font-family:"Barlow",sans-serif;font-size:14px;color:var(--ink);display:flex;gap:14px}
.social{right:96px;top:2572px;display:flex;gap:18px;font-family:"Barlow",sans-serif;font-size:13px;font-weight:600;color:var(--ink)}
.foot-rule{left:68px;top:2601px;width:1065px;height:1px;background:var(--line)}
.copy{left:80px;top:2616px;width:420px;font-size:13.5px;line-height:22px;color:var(--ink)}
.legal{right:100px;top:2617px;font-size:13.5px;color:var(--ink)}
</style>
</head>
<body>

<!-- header -->
<div class="abs brand">
  <div class="brand-mark"></div>
  <div>
    <div class="brand-name">BrightFloe</div>
    <div class="brand-tag">Contaminant control for industrial fluids</div>
  </div>
</div>
<div class="abs phone">
  <svg width="18" height="18" viewBox="0 0 24 24"><path fill="#1b1b1b" d="M6.6 10.8a15.1 15.1 0 0 0 6.6 6.6l2.2-2.2c.3-.3.7-.4 1-.2 1.1.4 2.3.6 3.6.6.6 0 1 .4 1 1V20c0 .6-.4 1-1 1A17 17 0 0 1 3 4c0-.6.4-1 1-1h3.5c.6 0 1 .4 1 1 0 1.3.2 2.5.6 3.6.1.3 0 .7-.2 1z"/></svg>
  (555)318-2094
</div>
<svg class="abs mail" width="18" height="14" viewBox="0 0 18 14"><rect width="18" height="14" rx="1.5" fill="#1b1b1b"/><path d="M1 2l8 6 8-6" stroke="#fff" stroke-width="1.6" fill="none"/></svg>
<div class="abs estimate"><span style="font-size:13px">›</span>Request An Estimate</div>
<nav class="abs nav">
  <span>Products</span><span>Benefits</span><span>Industries Served</span><span>About Us</span><span>Service &amp; Support</span>
</nav>

<!-- hero -->
<div class="abs hero" role="img" aria-label="Photo of a plant worker in hard hat and safety glasses on a factory floor"></div>
<h1 class="abs hero-title">Coolant Recycling System</h1>

<!-- product cards -->
<div class="card" style="left:75px;height:576px">
  <h3>Coolant Recycling Systems</h3>
  <div class="shot" role="img" aria-label="Product photo of a blue coolant recycling unit with drum" style="top:105px;height:200px;background:linear-gradient(160deg,#e6e9f0,#2f45a8 60%,#dfe1e6)"></div>
  <p style="top:353px">The FlowCycle™ Coolant Recycling Systems are based on decades-long successful fluid treatment practices, using the award-winning, multipatented BrightFloe® Systems approach to solving problems.</p>
  <div class="btn" style="top:503px">Learn More</div>
</div>
<div class="card" style="left:437px;height:548px">
  <h3>Magnetic Separators</h3>
  <div class="shot" role="img" aria-label="Product photo of two clear magnetic separator canisters" style="top:80px;height:245px;background:linear-gradient(180deg,#f2f3f5,#c9ccd2 60%,#3f63b8)"></div>
  <p style="top:353px">BrightFloe magnetic separators fit with our core philosophies: providing products that eliminate the use of filter consumables, are easy to implement, simple to operate, and require minimal maintenance.</p>
  <div class="btn" style="top:484px">Learn More</div>
</div>
<div class="card" style="left:797px;height:511px">
  <h3>Oil Water Separators</h3>
  <div class="shot" role="img" aria-label="Product photo of a blue oil water separator with pump stand" style="top:90px;height:235px;background:linear-gradient(160deg,#d9dbe0,#2a44a6 55%,#eceef2)"></div>
  <p style="top:353px">The BrightFloe “non-clogging” design allows for the separation of oils and settling of solids in one step.</p>
  <div class="btn" style="top:438px">Learn More</div>
</div>

<!-- trusted by -->
<h2 class="abs section-title" style="top:1258px">Trusted By</h2>
<div class="arrow" style="left:78px"><svg width="10" height="16"><path d="M8 2L2 8l6 6" stroke="#fff" stroke-width="2.4" fill="none"/></svg></div>
<div class="logo-box" style="left:121px">Marlowe Motors</div>
<div class="logo-box" style="left:316px">Vantessa</div>
<div class="logo-box" style="left:511px">Stellrand</div>
<div class="logo-box" style="left:706px">Corvane</div>
<div class="logo-box" style="left:900px">Aerolith</div>
<div class="arrow" style="left:1079px"><svg width="10" height="16"><path d="M2 2l6 6-6 6" stroke="#fff" stroke-width="2.4" fill="none"/></svg></div>

<!-- roi -->
<div class="abs roi" role="img" aria-label="Dark background photo of coolant spraying over a machined part"></div>
<h2 class="abs section-title" style="top:1585px;color:#fff">ROI Calculator</h2>
<p class="abs roi-text">By drastically reducing coolant costs and the cost of waste removal, our typical systems pay for themselves in 6-9 months. Check ot our ROI calculator to determine how much you can savie with our coolant recycling systems.</p>
<div class="btn" style="left:461px;top:1770px;width:279px;height:37px">Calculate Your Savings Now</div>

<!-- case study -->
<h2 class="abs section-title" style="top:1956px">Case Study</h2>
<div class="abs case-client">HCF</div>
<p class="abs case-text">Learn how Halvern Coldstream Fabrication saved 35-45% on their coolant recycling while increasing employee morale with a fully automated BrightFloe Recycling System</p>
<div class="btn" style="left:480px;top:2155px;width:206px;height:37px">Learn How They Did It</div>

<!-- newsletter -->
<div class="abs news" role="img" aria-label="Dark photo of workers in hard hats"></div>
<div class="abs news-title">STAY <span>UP TO DATE</span> WITH BRIGHTFLOE</div>
<div class="abs news-sub">SIGN UP TO GET OUR NEWSLETTER</div>
<div class="abs news-rule"></div>
<div class="abs email">Email Address</div>
<div class="btn subscribe">Subscribe</div>

<!-- footer -->
<div class="abs foot-links"><span>Contact</span><span>|</span><span>About</span><span>|</span><span>Blog</span></div>
<div class="abs social"><span>Follow</span><span>Connect</span><span>Watch</span></div>
<div class="abs foot-rule"></div>
<p class="abs copy">©2019 Meridian Separation Co. All Rights Reserved • Lakeport, Ohio • 800-555-0147 • support@brightfloe-example.com</p>
<p class="abs legal">Terms of Service &nbsp;|&nbsp; Privacy Policy &nbsp;|&nbsp; Sitemap</p>

</body>
</html>
```